Pictures required on web page

I would like change three existing pictures on my new website.

The site can be found here:
http://mossbottleroom.kestrelweb.com.au/

The three pictures to be changed are on the home page:
Purchase- Mixed Packs
Wine Club - Let Us Choose
Education- Wine Courses

I would like somthing stylish, classic and understated that fits in with the theme and feel of the site. I know stylish is a subjective thing. At the moment, the current picture makes the text difficult to read on a destop. Plus I don't think they are a perfect fit for our website anyway. I've attached a photo of our wine course room and also me in the store. Please, don't feel as though you have to use these pictures, but they're there if you want them. However I'm open to completely different photos/graphics to be used.

```html
<!DOCTYPE html>
<html lang="en">
<head>
<meta charset="utf-8">
<title>Mossbottle — Small winery specialist</title>
<link href="https://fonts.googleapis.com/css2?family=Roboto+Slab:wght@400;700&family=Roboto:wght@400;500&family=Arimo&display=swap" rel="stylesheet">
<style>
:root{
  --navy:#25335a;
  --navy-top:#2e3d66;
  --navy-dark:#131b2f;
  --tile-navy:#243256;
  --tile-red:#b9504c;
  --wine-red:#b64a48;
  --wine-red-soft:#cc7b7a;
  --grey-btn:#a4a4a4;
  --grey-btn-soft:#c8c8c8;
  --price:#3a4663;
  --price-soft:#6b7791;
  --text:#3a3a3a;
  --muted:#666;
  --rule:#e4e4e4;
  --white:#fff;
}
*{margin:0;padding:0;box-sizing:border-box}
html,body{width:1200px;height:994px;overflow:hidden;background:var(--white)}
body{position:relative;font-family:"Roboto",sans-serif;color:var(--text)}
.abs{position:absolute}

/* header */
.site-header{left:0;top:0;width:1200px;height:95px;background:linear-gradient(var(--navy-top),var(--navy))}
.brand{left:161px;top:16px;color:var(--white)}
.brand-name{font-family:"Roboto Slab",serif;font-weight:700;font-size:36px;line-height:40px;letter-spacing:.5px}
.brand-tagline{font-family:"Roboto Slab",serif;font-size:17px;line-height:20px;color:#dfe4ef}
.search{left:411px;top:31px;width:295px;height:31px;border:1px solid #6b7ba3;background:#34446e;border-radius:2px}
.search span{position:absolute;left:11px;top:6px;font-size:14px;color:#c3cbe0}
.search svg{position:absolute;right:8px;top:4px}
.top-links{left:710px;top:22px;display:flex}
.top-link{width:70px;text-align:center;color:#dde3f0;font-size:11px;letter-spacing:.3px;border-left:1px solid #3f4f7a;height:44px}
.top-link:first-child{border-left:none}
.top-link svg{display:block;margin:2px auto 6px}

/* nav */
.main-nav{left:0;top:95px;width:1200px;height:42px;background:var(--navy-dark)}
.main-nav ul{list-style:none;display:flex;position:absolute;left:162px;top:10px}
.main-nav li{color:var(--white);font-size:17px;font-weight:500;margin-right:23px}
.cart{left:907px;top:106px;color:var(--white);font-size:12px;display:flex;align-items:center;gap:8px}

/* feature tiles */
.tile{color:var(--white);text-align:center;overflow:hidden}
.tile-photo-blue{background:linear-gradient(135deg,#2d5aa3,#4c7fc6 55%,#26498a)}
.tile-photo-sepia{background:linear-gradient(160deg,#c7a571,#8e6c3f 60%,#5b4226)}
.tile-photo-gold{background:linear-gradient(180deg,#c9a46a,#b38c52 60%,#9a7441)}
.tile-kicker{font-family:"Roboto Slab",serif;font-size:15px;letter-spacing:2px;position:absolute;left:0;right:0}
.tile-title{font-family:"Roboto Slab",serif;font-weight:700;font-size:24px;letter-spacing:2.5px;position:absolute;left:0;right:0}
.tile-frame{position:absolute;border:1px solid rgba(255,255,255,.45)}
.tile-sub{font-family:"Roboto Slab",serif;font-size:13px;letter-spacing:1.5px;position:absolute;left:0;right:0}
.read-more{position:absolute;left:84px;top:200px;width:123px;height:33px;border:1px solid rgba(255,255,255,.8);font-family:"Roboto Slab",serif;font-size:13px;letter-spacing:2px;line-height:31px}

/* products */
.product{top:506px;height:440px;width:228px}
.product.is-active{border:1px solid #eee}
.product-photo{position:absolute;left:0;right:0;top:12px;height:210px}
.product-title{position:absolute;left:7px;top:222px;font-size:15px;line-height:18px;color:var(--text)}
.product-rule{position:absolute;left:7px;right:7px;top:243px;border-top:1px solid var(--rule)}
.product-desc{position:absolute;left:7px;right:6px;top:252px;height:78px;overflow:hidden;font-family:"Arimo",sans-serif;font-size:12.5px;line-height:16.5px;color:var(--text)}
.product-desc.short{color:var(--muted)}
.price{position:absolute;left:7px;top:348px;font-size:24px;color:var(--price)}
.price.soft{color:var(--price-soft)}
.btn{position:absolute;top:390px;height:36px;color:var(--white);font-family:"Roboto Slab",serif;font-size:13px;letter-spacing:1.5px;line-height:36px;text-align:center}
.btn-cart{left:7px;width:125px;background:var(--wine-red)}
.btn-view{left:138px;width:82px;background:var(--grey-btn)}
.is-active .btn-cart{background:var(--wine-red-soft)}
.is-active .btn-view{background:var(--grey-btn-soft)}

.pager{left:550px;top:958px;display:flex;gap:3px}
.pager i{width:17px;height:17px;border-radius:50%;background:linear-gradient(#f4f4f4,#d2d2d2);border:1px solid #c4c4c4}
.pager i.current{background:linear-gradient(#d8d8d8,#a9a9a9)}
.footer-rule{left:0;top:990px;width:1200px;height:4px;background:#c9d1e0}
</style>
</head>
<body>

<header class="site-header abs">
  <div class="brand abs">
    <div class="brand-name">Mossbottle</div>
    <div class="brand-tagline">Small winery specialist.</div>
  </div>
  <div class="search abs">
    <span>Search the Cellars</span>
    <svg width="22" height="22" viewBox="0 0 22 22" fill="none" stroke="#dfe4ef" stroke-width="2"><circle cx="9" cy="9" r="6"/><line x1="13.5" y1="13.5" x2="19" y2="19"/></svg>
  </div>
  <nav class="top-links abs">
    <div class="top-link"><svg width="16" height="14" viewBox="0 0 16 14" fill="#dde3f0"><path d="M8 0 0 7h2v7h4V9h4v5h4V7h2z"/></svg>HOME</div>
    <div class="top-link"><svg width="18" height="14" viewBox="0 0 18 14" fill="#dde3f0"><circle cx="5" cy="4" r="3"/><circle cx="13" cy="4" r="3"/><path d="M0 14c0-4 2-6 5-6s5 2 5 6zM8 14c0-4 2-6 5-6s5 2 5 6z"/></svg>ABOUT</div>
    <div class="top-link"><svg width="15" height="14" viewBox="0 0 15 14" fill="none" stroke="#dde3f0" stroke-width="1.6"><rect x="1" y="2" width="13" height="11"/><line x1="1" y1="5" x2="14" y2="5"/><line x1="4" y1="0" x2="4" y2="3"/><line x1="11" y1="0" x2="11" y2="3"/></svg>EVENTS</div>
    <div class="top-link"><svg width="14" height="14" viewBox="0 0 14 14"><circle cx="7" cy="7" r="5" fill="none" stroke="#dde3f0" stroke-width="3" stroke-dasharray="2.5 1.4"/><circle cx="7" cy="7" r="3" fill="#dde3f0"/><circle cx="7" cy="7" r="1.3" fill="#2e3d66"/></svg>ACCOUNT</div>
    <div class="top-link"><svg width="14" height="14" viewBox="0 0 14 14" fill="#dde3f0"><path d="M3 0 5.5 3.5 4 5.5c1 2 2.5 3.5 4.5 4.5L10.5 8.5 14 11l-1.5 2.5C7 13.5.5 7 .5 1.5z"/></svg>CONTACT</div>
  </nav>
</header>

<nav class="main-nav abs">
  <ul>
    <li>Red Wine</li><li>White Wine</li><li>Sparkling</li><li>Rosé</li><li>Old &amp; Rare</li><li>Stickies</li><li>Imported</li><li>Wine Club</li>
  </ul>
</nav>
<div class="cart abs">
  <svg width="20" height="17" viewBox="0 0 20 17" fill="#fff"><path d="M0 0h4l1 3h15l-3 8H6L3 2H0z"/><circle cx="7" cy="14.5" r="2"/><circle cx="16" cy="14.5" r="2"/></svg>
  <span>Shopping cart is empty</span>
</div>

<!-- feature tiles -->
<section class="tile tile-photo-blue abs" style="left:144px;top:150px;width:293px;height:197px" role="img" aria-label="Blue-toned photo of grapes on the vine for the wine courses promotion">
  <div class="tile-kicker" style="top:68px">EDUCATION</div>
  <div class="tile-title" style="top:92px">WINE COURSES</div>
</section>

<section class="tile tile-photo-sepia abs" style="left:453px;top:150px;width:293px;height:340px" role="img" aria-label="Sepia photo of the store owner among cellar shelves for the wine club">
  <div class="tile-kicker" style="top:107px">WINE CLUB</div>
  <div class="tile-title" style="top:133px">LET US CHOOSE</div>
  <div class="read-more">READ MORE</div>
</section>

<section class="tile tile-photo-gold abs" style="left:764px;top:150px;width:292px;height:197px" role="img" aria-label="Golden-toned photo of vineyard rows for mixed packs">
  <div class="tile-kicker" style="top:66px">PURCHASE</div>
  <div class="tile-title" style="top:92px">MIXED PACKS</div>
</section>

<section class="tile abs" style="left:144px;top:359px;width:293px;height:131px;background:var(--tile-red)">
  <div class="tile-frame" style="left:18px;top:19px;width:256px;height:93px"></div>
  <div class="tile-title" style="top:43px;font-weight:400;font-size:19px;letter-spacing:2px">FREE SHIPPING</div>
  <div class="tile-sub" style="top:70px">on orders over $200</div>
</section>

<section class="tile abs" style="left:764px;top:357px;width:292px;height:132px;background:var(--tile-navy)">
  <div class="tile-frame" style="left:17px;top:21px;width:256px;height:92px"></div>
  <div class="tile-title" style="top:43px;font-weight:400;font-size:19px;letter-spacing:2px">NEWSLETTER</div>
  <div class="tile-sub" style="top:70px;font-size:12.5px">join the newsletter for specials</div>
</section>

<!-- products -->
<article class="product is-active abs" style="left:138px">
  <div class="product-photo" role="img" aria-label="Bottle of red wine with a dark label" style="background:linear-gradient(90deg,#fff 33%,#6d6d6d 40%,#4a4a4a 50%,#6d6d6d 60%,#fff 67%)"></div>
  <div class="product-desc short" style="top:250px">New vintage of a great wine!</div>
  <div class="price soft">$70.40</div>
  <div class="btn btn-cart">ADD TO CART</div>
  <div class="btn btn-view">VIEW</div>
</article>

<article class="product abs" style="left:370px">
  <div class="product-photo" role="img" aria-label="Bottle of sparkling wine on a beige backdrop" style="left:60px;right:60px;background:linear-gradient(90deg,#e9dcc6 20%,#5b5a3c 40%,#3c3b28 50%,#5b5a3c 60%,#e9dcc6 80%)"></div>
  <div class="product-title">Classique NV</div>
  <div class="product-rule"></div>
  <div class="product-desc">The Cuvée Classique strikes a clear house note with fine mineral/salt depths. The Cuvée Classique (80 percent Chardonnay, 20 percent Pinot Noir) is a premier cru from Aubrel. It's extremely dry and very fresh with a long clean finish.</div>
  <div class="price">$88.00</div>
  <div class="btn btn-cart">ADD TO CART</div>
  <div class="btn btn-view">VIEW</div>
</article>

<article class="product abs" style="left:603px">
  <div class="product-photo" role="img" aria-label="Bottle of red wine with a red illustrated label" style="background:linear-gradient(90deg,#fff 35%,#3a1a1e 42%,#b8453f 50%,#3a1a1e 58%,#fff 65%)"></div>
  <div class="product-title">Creekbed Red 2010</div>
  <div class="product-rule"></div>
  <div class="product-desc">Top 100- Harbour City Wine Challenge 2012, Blue-Gold- Harbour City Wine Challenge 2012, Gold- Southern Cross Wine Show 2011</div>
  <div class="price">$16.45</div>
  <div class="btn btn-cart">ADD TO CART</div>
  <div class="btn btn-view">VIEW</div>
</article>

<article class="product abs" style="left:835px">
  <div class="product-photo" role="img" aria-label="Bottle of white wine with a cream label" style="background:linear-gradient(90deg,#fff 35%,#3e3f22 42%,#e8e2cf 50%,#3e3f22 58%,#fff 65%)"></div>
  <div class="product-title">Sauvignon 2012</div>
  <div class="product-rule"></div>
  <div class="product-desc">With a pale straw yellow colour, this has melon &amp; white peach flavours that continue through the palate with lees complexity that integrates beautifully with the lemon sorbet like acidity. This zesty wine finishes clean and long.</div>
  <div class="price">$0.00</div>
  <div class="btn btn-cart">ADD TO CART</div>
  <div class="btn btn-view">VIEW</div>
</article>

<div class="pager abs"><i></i><i></i><i></i><i class="current"></i><i></i></div>
<div class="footer-rule abs"></div>

</body>
</html>
```